Business Card Design

Hoping for a black background business card, minimalistic design.
With the Marble Crest logo you created in white.

I would like to include:
My Name and title
Address (street address)
Reception: (phone number)
Fax: (fax number)
Reception: (email address)
Direct email: (email address)
Instagram: (ig handle)

```html
<!DOCTYPE html>
<html lang="en">
<head>
<meta charset="UTF-8">
<title>Marble Crest — Business Card</title>
<link href="https://fonts.googleapis.com/css2?family=Oswald:wght@300;400;600&display=swap" rel="stylesheet">
<style>
  :root {
    --backdrop: #d4d4d4;
    --backdrop-edge: #b9b9b9;
    --card: #0c0c0c;
    --card-glow: #1c1c1c;
    --ink: #ffffff;
    --ink-muted: #8a8a8a;
  }
  * { margin: 0; padding: 0; box-sizing: border-box; }
  html, body {
    width: 1200px;
    height: 876px;
    overflow: hidden;
  }
  body {
    position: relative;
    background: radial-gradient(ellipse at 55% 40%, var(--backdrop) 0%, var(--backdrop-edge) 100%);
    font-family: "Oswald", sans-serif;
    color: var(--ink);
  }
  .card {
    position: absolute;
    width: 560px;
    height: 320px;
    background: radial-gradient(ellipse at 40% 35%, var(--card-glow) 0%, var(--card) 70%);
    box-shadow: 0 18px 40px rgba(0,0,0,0.35);
  }
  .card--front { left: 590px; top: 110px; }
  .card--back  { left: 50px;  top: 446px; }

  .brand {
    position: absolute;
    font-weight: 400;
    text-transform: uppercase;
    color: var(--ink);
    white-space: nowrap;
    line-height: 1;
  }
  .card--front .brand {
    left: 0;
    right: 0;
    top: 138px;
    text-align: center;
    font-size: 34px;
    letter-spacing: 2px;
  }
  .card--back .brand {
    right: 36px;
    top: 150px;
    font-size: 20px;
    letter-spacing: 1px;
  }

  .holder {
    position: absolute;
    left: 36px;
    top: 30px;
  }
  .holder__name {
    font-size: 30px;
    font-weight: 600;
    text-transform: uppercase;
    line-height: 1.1;
  }
  .holder__title {
    font-size: 14px;
    font-weight: 300;
    color: var(--ink-muted);
    text-transform: uppercase;
    margin-top: 4px;
  }
  .contact {
    position: absolute;
    list-style: none;
    font-size: 13px;
    font-weight: 400;
    text-transform: uppercase;
    line-height: 1.35;
  }
  .contact--personal { left: 36px; top: 126px; }
  .contact--office { right: 36px; bottom: 30px; text-align: left; }
</style>
</head>
<body>
  <section class="card card--front" aria-label="Card front">
    <p class="brand">Marble Crest</p>
  </section>

  <section class="card card--back" aria-label="Card back">
    <div class="holder">
      <h1 class="holder__name">Full Name</h1>
      <p class="holder__title">Title</p>
    </div>
    <ul class="contact contact--personal">
      <li>Address: (street address)</li>
      <li>Direct email: (email address)</li>
      <li>Instagram: (ig handle)</li>
    </ul>
    <p class="brand">Marble Crest</p>
    <ul class="contact contact--office">
      <li>Reception: (phone number)</li>
      <li>Fax: (fax number)</li>
      <li>Reception: (email address)</li>
    </ul>
  </section>
</body>
</html>
```